Custom Wordpress Theme Needed

We need a custom Wordpress theme built with the following features:

1. Flat style design
2. Fully responsive - built for mobile and tablets first; bootstrap or other framework used
3. Flexible - comes with homepage layouts for portfolios, agencies, and magazines
4. Built in 'contact' and 'about us' styling
5. Pre-populated pages and content, including reusable images
6. Multiple slider options

We are completely open to your creativity as far as the overall design style is concerned, but some of our favorites are:
http://themes.plovaro.com/themeselector/?theme=TideBoard
http://www.kelmora.ru/flatmagazine/
http://quarnwellbox.com/wp/velta/intro/
http://theme.dovrask.net/second/

Most unique and in-depth style wins!

Reason: We need more designs!

Reason: Waiting on final submissions and revisions. Thanks!

```html
<!DOCTYPE html>
<html lang="en">
<head>
<meta charset="utf-8">
<title>Technology Guru's — Digital Agency</title>
<link rel="stylesheet" href="https://fonts.googleapis.com/css2?family=Oswald:wght@400;500;600&family=Open+Sans:wght@400;600&display=swap">
<style>
:root{
  --ink:#2b2f33;
  --dark:#34383c;
  --slate:#3c4650;
  --muted:#8a8f94;
  --line:#d9dcdf;
  --paper:#ffffff;
  --mist:#ececec;
  --accent:#e8552b;
  --sky:#2a7fc8;
  --head:'Oswald',sans-serif;
  --body:'Open Sans',sans-serif;
}
*{box-sizing:border-box;margin:0;padding:0}
html,body{width:1200px;height:4300px;overflow:hidden}
body{font-family:var(--body);color:var(--ink);background:var(--paper);position:relative}
section,header,footer{position:absolute;left:0;width:1200px}

/* navigation */
.site-nav{top:0;height:68px;background:var(--paper);display:flex;align-items:center;padding:0 140px}
.brand{display:flex;align-items:center;gap:8px;font-family:var(--head);font-size:15px;color:var(--ink);font-weight:400}
.brand-dot{width:20px;height:20px;border-radius:50%;background:var(--accent)}
.menu{margin-left:auto;display:flex;gap:42px;list-style:none;font-family:var(--head);font-size:12px;letter-spacing:.5px;color:var(--ink)}

/* hero */
.hero{top:68px;height:472px;background:linear-gradient(180deg,#8aa6bd 0%,#c9b4a8 30%,#6f7d8c 55%,#3a4b5c 80%,#54697c 100%);text-align:center;color:#fff}
.hero-title{font-family:var(--head);font-weight:500;font-size:56px;line-height:66px;letter-spacing:2px;padding-top:70px}
.hero-sub{font-family:var(--head);font-size:17px;letter-spacing:4px;margin-top:16px}
.btn-outline{display:inline-block;border:2px solid #fff;font-family:var(--head);font-size:15px;letter-spacing:2px;padding:6px 28px;margin-top:26px;color:#fff;background:rgba(40,50,60,.5)}

/* services */
.services{top:540px;height:520px;background:var(--mist)}
.service-card{position:absolute;top:68px;width:262px;height:352px;background:var(--paper);text-align:center;padding:30px 30px}
.service-icon{width:92px;height:92px;border-radius:50%;background:var(--slate);margin:0 auto;display:flex;align-items:center;justify-content:center}
.service-card h3{font-family:var(--head);font-weight:500;font-size:17px;letter-spacing:1px;margin:42px 0 18px}
.service-card p{font-size:13px;line-height:20px;color:var(--ink)}

/* statement */
.statement{top:1060px;height:300px;background:linear-gradient(180deg,#dfe3e7,#b8c0c8 50%,#d8dde2);display:flex;align-items:center;justify-content:center;text-align:center}
.statement p{font-family:var(--head);font-size:36px;line-height:46px;letter-spacing:2px;color:#fff;text-shadow:0 0 6px rgba(80,90,100,.5)}

/* portfolio */
.portfolio{top:1360px;height:940px;background:var(--paper);text-align:center}
.boxed-title{display:inline-block;background:var(--slate);color:#fff;font-family:var(--head);font-weight:600;font-size:36px;letter-spacing:2px;padding:8px 40px;border:4px solid var(--paper);outline:3px solid var(--slate);margin-top:52px}
.lede{font-size:13px;line-height:20px;color:var(--muted);text-transform:uppercase;width:460px;margin:22px auto 0}
.filters{display:flex;justify-content:center;margin-top:52px;list-style:none}
.filters li{font-family:var(--head);font-size:12px;letter-spacing:1px;border:1px solid var(--line);padding:6px 0;width:96px;margin:0 4px}
.filters li.active{background:var(--dark);color:#fff;border-color:var(--dark)}
.work-grid{position:absolute;left:60px;top:348px;width:1080px;display:grid;grid-template-columns:repeat(4,250px);column-gap:26px;row-gap:100px}
.work-thumb{height:172px}
.work-item h4{font-family:var(--head);font-weight:400;font-size:14px;margin-top:14px;letter-spacing:.5px}
.work-item span{font-size:11px;color:var(--muted)}
.t-bridge{background:linear-gradient(160deg,#3a1a6b,#c84ab0 55%,#2a1a4a)}
.t-mountain{background:linear-gradient(180deg,#d84a3a,#7a3a5a 55%,#2a2a40)}
.t-tundra{background:linear-gradient(180deg,#d8a070,#e8eef4 50%,#a9bfd6)}
.t-sea{background:linear-gradient(160deg,#0a2a7a,#3a6ad0 60%,#0a1a4a)}

/* testimonial */
.testimonial{top:2300px;height:292px;background:linear-gradient(90deg,#e6f0fa 0%,#7fb3e0 40%,#2a7fc8 100%)}
.person{position:absolute;left:120px;top:24px;width:280px;height:268px;background:linear-gradient(180deg,#5b4b44,#2a2c30)}
.quote{position:absolute;left:440px;top:42px;width:680px;color:#fff;font-family:var(--head);font-size:19px;line-height:34px;letter-spacing:1px;font-style:normal}
.quote-actions{position:absolute;left:410px;top:178px;display:flex;gap:44px}
.quote-actions span{border:2px solid #fff;color:#fff;font-family:var(--head);font-size:14px;letter-spacing:2px;width:200px;text-align:center;padding:4px 0}

/* team */
.team{top:2592px;height:728px;background:var(--paper);text-align:center}
.team h2{font-family:var(--head);font-weight:500;font-size:40px;margin-top:40px}
.team .kicker{font-family:var(--head);font-size:15px;letter-spacing:1px;margin-top:8px}
.member{position:absolute;top:200px;width:252px;height:408px;background:var(--paper);box-shadow:0 0 6px rgba(0,0,0,.18);padding:18px 22px;text-align:center}
.member-photo{width:192px;height:148px;margin:0 auto;background:linear-gradient(180deg,#cfc6be,#8e7f74)}
.member p{font-size:12px;line-height:18px;color:var(--muted);margin-top:24px}
.member h5{font-family:var(--head);font-weight:400;font-size:14px;margin-top:22px;text-align:left;border-bottom:1px solid var(--line);padding-bottom:6px}
.member ul{list-style:none;font-size:12px;color:var(--ink)}
.member li{border-bottom:1px solid var(--line);padding:6px 0}

/* contact banner */
.contact-banner{top:3320px;height:320px;background:linear-gradient(180deg,#5a5e62,#2a2d30 60%,#45484b);text-align:center;color:#fff}
.contact-banner .boxed-title{background:var(--dark);outline-color:#fff;border-color:var(--dark);margin-top:60px}
.contact-banner p{font-family:var(--head);font-size:19px;line-height:28px;letter-spacing:1px;width:600px;margin:20px auto 0}

/* form */
.contact-form{top:3640px;height:500px;background:var(--paper);padding:60px 150px 0}
.field-row{display:flex;gap:40px}
.field{flex:1}
.field label,.message label{font-size:11px;color:var(--ink);display:block}
.input{height:34px;border-bottom:2px solid var(--line);background:#fafafa}
.message{margin-top:26px}
.textarea{height:218px;border:1px solid var(--line);background:#fafafa;margin-top:6px}
.form-foot{display:flex;align-items:center;margin-top:22px;font-size:11px;color:var(--muted)}
.check{width:12px;height:12px;border:1px solid var(--muted);margin-right:8px}
.submit{margin-left:auto;background:var(--accent);color:#fff;font-family:var(--head);font-size:12px;letter-spacing:1px;padding:5px 18px}

/* footer */
.site-footer{top:4140px;height:160px;background:var(--dark);text-align:center;color:#cfd2d5}
.socials{display:flex;justify-content:center;gap:34px;padding-top:38px}
.socials span{width:42px;height:42px;border-radius:50%;background:#fff}
.legal{display:flex;justify-content:center;gap:60px;font-size:11px;margin-top:34px;letter-spacing:.5px}
</style>
</head>
<body>

<header class="site-nav">
  <div class="brand"><span class="brand-dot"></span>Company</div>
  <ul class="menu"><li>HOME</li><li>ABOUT US</li><li>OUR CLIENTS</li><li>WORK</li><li>PORTFOLIO</li><li>CONTACT US</li></ul>
</header>

<section class="hero" role="img" aria-label="Mountain range at sunrise above a misty lake">
  <h1 class="hero-title">HELLO,<br>WE ARE TECHNOLOGY GURU'S</h1>
  <div class="hero-sub">AWARD WINNING DIGITAL AGENCY</div>
  <span class="btn-outline">VIEW WORK</span>
</section>

<section class="services">
  <article class="service-card" style="left:140px">
    <div class="service-icon"><svg width="46" height="46" viewBox="0 0 46 46"><circle cx="23" cy="23" r="20" fill="#fff"/><rect x="13" y="16" width="20" height="13" rx="2" fill="#3c4650"/><rect x="20" y="30" width="6" height="4" fill="#3c4650"/></svg></div>
    <h3>DIGITAL SOLUTIONS</h3>
    <p>We build clean digital products that help brands grow across every screen and device.</p>
  </article>
  <article class="service-card" style="left:469px">
    <div class="service-icon"><svg width="46" height="46" viewBox="0 0 46 46"><circle cx="23" cy="23" r="20" fill="#fff"/><circle cx="23" cy="23" r="13" fill="none" stroke="#3c4650" stroke-width="3"/><path d="M23 12 L27 23 L23 34 L19 23 Z" fill="#3c4650"/></svg></div>
    <h3>TECHNOLOGY START UP</h3>
    <p>From first idea to launch, we guide young teams through planning, design and steady growth.</p>
  </article>
  <article class="service-card" style="left:798px">
    <div class="service-icon"><svg width="46" height="46" viewBox="0 0 46 46"><circle cx="23" cy="23" r="20" fill="#fff"/><path d="M23 23 L23 8 A15 15 0 1 1 8 23 Z" fill="#3c4650"/></svg></div>
    <h3>SEO OPTIMIZING</h3>
    <p>Smart search work that brings the right visitors to your site and keeps them coming back.</p>
  </article>
</section>

<section class="statement" role="img" aria-label="Blurred city skyline">
  <p>THE REASON WE LEFT IT IN THE MARKETING IS DESIGN<br>IT'S REALLY THAT SIMPLE</p>
</section>

<section class="portfolio">
  <h2 class="boxed-title">PORTFOLIO</h2>
  <p class="lede">Lorem ipsum is mostly a part of a latin text by the classical author and philosopher Cicero.</p>
  <ul class="filters"><li class="active">WEB</li><li>LOGO</li><li>3D</li><li>ANIMATION</li><li>PRINT</li></ul>
  <div class="work-grid">
    <div class="work-item"><div class="work-thumb t-bridge" role="img" aria-label="Fireworks over a bridge at night"></div><h4>FIREWORKS BRIDGE</h4><span>Web design</span></div>
    <div class="work-item"><div class="work-thumb t-mountain" role="img" aria-label="Mountain lake at sunset"></div><h4>SIERRA MOUNTAIN SET</h4><span>Web design</span></div>
    <div class="work-item"><div class="work-thumb t-tundra" role="img" aria-label="Snow covered trees"></div><h4>FROZEN TUNDRA</h4><span>Web design</span></div>
    <div class="work-item"><div class="work-thumb t-sea" role="img" aria-label="Lionfish underwater"></div><h4>LIONFISH SEA</h4><span>Web design</span></div>
    <div class="work-item"><div class="work-thumb t-bridge" role="img" aria-label="Fireworks over a bridge at night"></div><h4>FIREWORKS BRIDGE</h4><span>Web design</span></div>
    <div class="work-item"><div class="work-thumb t-mountain" role="img" aria-label="Mountain lake at sunset"></div><h4>SIERRA MOUNTAIN SET</h4><span>Web design</span></div>
    <div class="work-item"><div class="work-thumb t-tundra" role="img" aria-label="Snow covered trees"></div><h4>FROZEN TUNDRA</h4><span>Web design</span></div>
    <div class="work-item"><div class="work-thumb t-sea" role="img" aria-label="Lionfish underwater"></div><h4>LIONFISH SEA</h4><span>Web design</span></div>
  </div>
</section>

<section class="testimonial">
  <div class="person" role="img" aria-label="Smiling businesswoman in a dark suit"></div>
  <blockquote class="quote">“ I APPRECIATE THE SERVICE LEVEL THAT WE'VE EXPERIENCED FROM THE LUMORA TEAM. NOT ONLY WERE THEY EXTREMELY RESPONSIVE, BUT THEIR STAFF IS VERY PROFESSIONAL ”</blockquote>
  <div class="quote-actions"><span>CONTACT US</span><span>MEET THE TEAM</span><span>SERVICES</span></div>
</section>

<section class="team">
  <h2>THE TEAM</h2>
  <div class="kicker">PROFESSIONAL AGENCY SERVICE IN THE HEART OF MELBOURNE</div>
  <article class="member" style="left:140px">
    <div class="member-photo" role="img" aria-label="Portrait of a team member"></div>
    <p>Strategist with ten years of agency work, focused on brand clarity, research and digital growth for clients.</p>
    <h5>WHAT WE OFFER</h5>
    <ul><li>Research</li><li>Strategy</li><li>Design</li></ul>
  </article>
  <article class="member" style="left:474px">
    <div class="member-photo" role="img" aria-label="Portrait of a team member"></div>
    <p>Designer who shapes calm, useful interfaces and turns complex ideas into simple screens for every device.</p>
    <h5>WHAT WE OFFER</h5>
    <ul><li>Research</li><li>Strategy</li><li>Design</li></ul>
  </article>
  <article class="member" style="left:808px">
    <div class="member-photo" role="img" aria-label="Portrait of a team member"></div>
    <p>Project lead keeping teams on time and on budget, with a sharp eye for detail and lasting client care.</p>
    <h5>WHAT WE OFFER</h5>
    <ul><li>Research</li><li>Strategy</li><li>Design</li></ul>
  </article>
</section>

<section class="contact-banner" role="img" aria-label="Open plan office with desks and computers">
  <h2 class="boxed-title">CONTACT US</h2>
  <p>LOREM IPSUM IS MOSTLY A PART OF A LATIN TEXT BY THE CLASSICAL AUTHOR AND PHILOSPHER CICERO</p>
</section>

<section class="contact-form">
  <div class="field-row">
    <div class="field"><label>Name</label><div class="input"></div></div>
    <div class="field"><label>Email</label><div class="input"></div></div>
  </div>
  <div class="message"><label>Message</label><div class="textarea"></div></div>
  <div class="form-foot"><span class="check"></span>Send me a copy of this message by email<span class="submit">SUBMIT</span></div>
</section>

<footer class="site-footer">
  <div class="socials"><span></span><span></span><span></span><span></span></div>
  <div class="legal"><span>© 2014 Company. All rights reserved</span><span>|</span><span>hello@company.com</span><span>|</span><span>Terms of use | Privacy policy</span></div>
</footer>

</body>
</html>
```